Health Care Service Company Flyer

Company name: Tall Orchard Studio
Slogan: Find out what you're made of
Website: tallorchardstudio.ca

I need the flyer to contain the company name (will provide logo source file ASAP), the slogan in large font and a "find out more at orchardstudio.ca"

Other important data to include in the flyer is:
Four bullet points with the following information:
*Track performance and fitness results over time
*Develop proprietary exercise and dietary programs based on actionable data
*Track muscle atrophy from injury, as well as muscle gain during rehabilitation
*Reveal imbalances in muscle symmetry and strength, flexibility, and joint mechanics

I also need the following information conveyed somewhere on the flyer:
*Body Fat, Muscle Mass, and Bone Density Measurements
• Over 50 data points generated in each 10 minute scan
*Call XXX-XXX-XXX to book an appointment today

DEXA Body Composition Services.
Get scanned today.

See example of competitor flyers in the images to get an example of the images and information we are trying to convey

Target Market(s)

athletes, fitness enthusiast, crossfit

Industry/Entity Type

Health And Wellness

Colors
33a6d7
acd036

Requirements
Nice to have
• Prefer images be general health and wellness related - in other words, individuals who look healthy, but are not abnormally muscular
Should not have
• Shirtless models, No big muscles,

```html
<!DOCTYPE html>
<html lang="en">
<head>
<meta charset="utf-8">
<title>Tall Orchard Studio – DEXA Body Composition Flyer</title>
<link rel="stylesheet" href="https://fonts.googleapis.com/css2?family=Montserrat:wght@300;400;500;600;700;800;900&family=Permanent+Marker&family=Kaushan+Script&display=swap">
<style>
  :root {
    --brand-blue: #33a6d7;
    --sky-blue: #22bdeb;
    --lime: #acd036;
    --navy: #2e3192;
    --purple: #4f1a5e;
    --magenta: #e84a8c;
    --ink: #111111;
    --paper: #ffffff;
    --photo-light: #eef0f2;
    --photo-mid: #d9dcdf;
  }
  * { box-sizing: border-box; margin: 0; padding: 0; }
  html, body {
    width: 1078px; height: 1200px; overflow: hidden;
    background: var(--paper);
    font-family: "Montserrat", Arial, sans-serif;
  }
  .flyer {
    position: absolute; left: 118px; top: 4px;
    width: 1031px; height: 1450px;
    transform: scale(0.8166); transform-origin: 0 0;
    overflow: hidden;
  }
  .photo {
    position: absolute; inset: 0;
    background: linear-gradient(160deg, var(--photo-light) 0%, #f7f7f7 40%, var(--photo-mid) 100%);
  }
  .shapes { position: absolute; inset: 0; }
  .brand-name {
    position: absolute; left: 250px; top: 38px; width: 760px;
    text-align: center; color: var(--lime);
    font-weight: 800; font-size: 52px; letter-spacing: 4px; text-transform: uppercase;
  }
  .slogan-find {
    position: absolute; left: 430px; top: 236px;
    color: var(--brand-blue); font-weight: 300; font-size: 66px; letter-spacing: 1px;
  }
  .slogan-what {
    position: absolute; left: 415px; top: 302px; width: 335px; height: 108px;
    background: var(--lime); box-shadow: 3px 4px 6px rgba(0,0,0,.25);
    color: var(--navy); font-weight: 400; font-size: 106px; line-height: 108px;
    padding-left: 18px; letter-spacing: -2px; white-space: nowrap;
  }
  .slogan-youre {
    position: absolute; left: 440px; top: 420px;
    color: var(--ink); font-weight: 900; font-size: 92px; letter-spacing: -1px;
  }
  .slogan-made {
    position: absolute; left: 430px; top: 515px;
    color: var(--ink); font-family: "Permanent Marker", "Kaushan Script", cursive; font-size: 112px;
    line-height: 1.1; transform: skewX(-12deg); letter-spacing: -4px;
  }
  .slogan-of {
    position: absolute; left: 748px; top: 530px;
    color: var(--ink); font-weight: 400; font-size: 92px;
  }
  .benefits {
    position: absolute; left: 40px; top: 734px; width: 960px;
    list-style: none; text-align: center;
    color: var(--ink); font-weight: 700; font-size: 21px; line-height: 27.5px;
  }
  .benefits li::before { content: "\25C6"; margin-right: 2px; }
  .service-callout {
    position: absolute; left: 60px; top: 934px; width: 500px;
    text-align: center; color: var(--ink); font-weight: 600; font-size: 25px; line-height: 32px;
  }
  .tagline-look {
    position: absolute; left: 400px; top: 1000px; line-height: 1.2;
    color: var(--paper); font-family: "Kaushan Script", cursive; font-size: 130px;
    text-shadow: 2px 3px 4px rgba(0,0,0,.3);
  }
  .tagline-and {
    position: absolute; left: 508px; top: 1150px; line-height: 1;
    color: var(--ink); font-weight: 400; font-size: 52px;
  }
  .tagline-feel {
    position: absolute; left: 630px; top: 1090px; line-height: 1.2;
    color: var(--paper); font-family: "Kaushan Script", cursive; font-size: 130px;
    text-shadow: 2px 3px 4px rgba(0,0,0,.3);
  }
  .measurements {
    position: absolute; left: 268px; top: 1270px;
    list-style: none; color: var(--ink); font-weight: 400; font-size: 20px; line-height: 25px;
  }
  .measurements li::before { content: "\25C6"; margin-right: 22px; }
  .website-line {
    position: absolute; left: 0; top: 1386px; width: 1031px;
    text-align: center; color: var(--ink); font-weight: 600; font-size: 22px;
  }
  .website-line strong { color: var(--navy); font-weight: 700; }
</style>
</head>
<body>
  <main class="flyer">
    <div class="photo" role="img" aria-label="Photo of a woman in white doing a side-stretch yoga pose on a mat in a white brick studio"></div>

    <svg class="shapes" width="1031" height="1450" viewBox="0 0 1031 1450" aria-hidden="true">
      <defs>
        <linearGradient id="header-fill" x1="0" y1="0" x2="0" y2="1">
          <stop offset="0" stop-color="#4f1a5e"/>
          <stop offset="1" stop-color="#e84a8c"/>
        </linearGradient>
      </defs>
      <path d="M20 0 H1031 V150 L820 232 Q780 246 740 232 L250 80 Z" fill="url(#header-fill)"/>
      <polygon points="0,0 250,82 0,375" fill="#33a6d7"/>
      <polyline points="775,345 972,345 972,670 610,670" fill="none" stroke="#33a6d7" stroke-width="3"/>
      <polygon points="0,960 250,1075 0,1165" fill="#22bdeb"/>
      <polygon points="0,1165 1031,820 1031,1450 0,1450" fill="#acd036"/>
    </svg>

    <h1 class="brand-name">Tall Orchard Studio</h1>

    <div class="slogan-find">find out</div>
    <div class="slogan-what">WHAT</div>
    <div class="slogan-youre">YOU'RE</div>
    <div class="slogan-made">MADE</div>
    <div class="slogan-of">of</div>

    <ul class="benefits">
      <li>Track performance and fitness results over time</li>
      <li>Develop proprietary exercise and dietary programs based on actionable data</li>
      <li>Track muscle atrophy from injury, as well as muscle gain during rehabilitation</li>
      <li>Reveal imbalances in muscle symmetry and strength, flexibility, and joint mechanics</li>
    </ul>

    <p class="service-callout">DEXA Body Composition Services.<br>Get scanned today.</p>

    <div class="tagline-look">Look</div>
    <div class="tagline-and">and</div>
    <div class="tagline-feel">Feel</div>

    <ul class="measurements">
      <li>Body Fat, Muscle Mass, and Bone Density Measurements</li>
      <li>Over 50 data points generated in each 10 minute scan</li>
      <li>Call XXX-XXX-XXX to book an appointment today</li>
    </ul>

    <p class="website-line">Find out more at <strong>orchardstudio.ca</strong></p>
  </main>
</body>
</html>
```